Trade show Banner to be displayed on vertical stand

We are an IT company that specializes in working with Manufacturing companies and manufacturing plants. We need two banners designed for a manufacturing trade show. The design needs to be designed using the supplied template file. Also the design needs to communicate graphically that we specialize in working with manufacturing plants. Also they should communicate that out services include: IT Services, Network, Voice, Data

Target Market(s)

Manufacturing companies

Industry/Entity Type

Manufacturing

Requirements
Must have
• Clear message, clear graphic message. Must be designed with included templates
Nice to have
• Company colors need to be used, but additional colors can be used

```html
<!DOCTYPE html>
<html lang="en">
<head>
<meta charset="utf-8">
<title>Forgeline Networks – Trade Show Banner</title>
<link rel="stylesheet" href="https://fonts.googleapis.com/css2?family=Exo+2:wght@400;500;600&display=swap">
<style>
  :root {
    --brand-blue: #2586c7;
    --brand-blue-deep: #1f78b8;
    --panel-light: #eef0f6;
    --panel-shade: #d8ddec;
    --arc-white: #f4f6fa;
    --ink: #1c1c1e;
    --page: #efefef;
  }
  html, body {
    margin: 0;
    padding: 0;
    width: 1200px;
    height: 2161px;
    overflow: hidden;
    background: var(--page);
  }
  .canvas {
    position: relative;
    width: 1200px;
    height: 2161px;
  }
  .banner {
    position: absolute;
    left: 209.5px;
    top: 40px;
    width: 468px;
    height: 1247px;
    transform: scale(1.669);
    transform-origin: top left;
    overflow: hidden;
    background: var(--brand-blue);
    font-family: "Exo 2", sans-serif;
    color: var(--ink);
  }
  .banner-backdrop {
    position: absolute;
    inset: 0;
    width: 468px;
    height: 1247px;
  }
  .brand {
    position: absolute;
    left: 48px;
    top: 368px;
    display: flex;
    align-items: center;
    gap: 18px;
  }
  .brand-dot {
    width: 84px;
    height: 84px;
    border-radius: 50%;
    background: var(--brand-blue);
    flex: none;
  }
  .brand-name {
    margin: 0;
    font-family: "Exo 2", sans-serif;
    font-weight: 600;
    font-size: 44px;
    line-height: 42px;
    color: var(--brand-blue);
    letter-spacing: 0.5px;
  }
  .services {
    position: absolute;
    left: 160px;
    top: 520px;
    margin: 0;
    padding: 0;
    list-style: none;
  }
  .service {
    height: 126px;
  }
  .service-title {
    display: flex;
    align-items: center;
    gap: 8px;
    margin: 0;
    font-weight: 500;
    font-size: 31px;
    line-height: 40px;
    color: var(--ink);
  }
  .service-icon {
    width: 30px;
    height: 30px;
    flex: none;
  }
  .service-text {
    margin: 2px 0 0 0;
    font-size: 15px;
    line-height: 23px;
    font-weight: 400;
    color: var(--ink);
  }
</style>
</head>
<body>
<div class="canvas">
  <section class="banner" aria-label="Forgeline Networks trade show banner">
    <svg class="banner-backdrop" viewBox="0 0 468 1247" aria-hidden="true">
      <defs>
        <linearGradient id="panelFill" x1="0" y1="0" x2="0" y2="1">
          <stop offset="0" stop-color="#f1f3f8"/>
          <stop offset="0.55" stop-color="#dde2ef"/>
          <stop offset="1" stop-color="#e8ebf3"/>
        </linearGradient>
      </defs>
      <rect width="468" height="1247" fill="var(--brand-blue)"/>
      <circle cx="540" cy="612" r="548" fill="var(--arc-white)"/>
      <circle cx="534" cy="618" r="532" fill="var(--brand-blue)"/>
      <circle cx="530" cy="616" r="522" fill="url(#panelFill)"/>
    </svg>

    <div class="brand">
      <span class="brand-dot"></span>
      <h1 class="brand-name">forgeline<br>networks</h1>
    </div>

    <ul class="services">
      <li class="service">
        <h2 class="service-title">
          <svg class="service-icon" viewBox="0 0 30 30" aria-hidden="true">
            <path d="M4 7 L22 3 L26 5 L26 27 L8 27 L4 25 Z" fill="var(--brand-blue)"/>
          </svg>
          IT Services
        </h2>
        <p class="service-text">Lorem ipsum dolor sit amet,<br>consectetuer adipiscing elit, sed diam</p>
      </li>
      <li class="service">
        <h2 class="service-title">
          <svg class="service-icon" viewBox="0 0 30 30" aria-hidden="true">
            <g stroke="var(--brand-blue)" stroke-width="2">
              <line x1="15" y1="15" x2="15" y2="4"/>
              <line x1="15" y1="15" x2="4" y2="11"/>
              <line x1="15" y1="15" x2="26" y2="11"/>
              <line x1="15" y1="15" x2="7" y2="26"/>
              <line x1="15" y1="15" x2="23" y2="26"/>
            </g>
            <g fill="var(--brand-blue)">
              <circle cx="15" cy="15" r="5"/>
              <circle cx="15" cy="4" r="2.5"/>
              <circle cx="4" cy="11" r="2.5"/>
              <circle cx="26" cy="11" r="2.5"/>
              <circle cx="7" cy="26" r="2.5"/>
              <circle cx="23" cy="26" r="2.5"/>
            </g>
          </svg>
          Network
        </h2>
        <p class="service-text">Lorem ipsum dolor sit amet,<br>consectetuer adipiscing elit, sed diam</p>
      </li>
      <li class="service">
        <h2 class="service-title">
          <svg class="service-icon" viewBox="0 0 30 30" aria-hidden="true">
            <rect x="11" y="2" width="8" height="16" rx="4" fill="var(--brand-blue)"/>
            <path d="M7 13 a8 8 0 0 0 16 0" fill="none" stroke="var(--brand-blue)" stroke-width="2"/>
            <line x1="15" y1="21" x2="15" y2="27" stroke="var(--brand-blue)" stroke-width="2"/>
            <line x1="10" y1="27" x2="20" y2="27" stroke="var(--brand-blue)" stroke-width="2"/>
          </svg>
          Voice
        </h2>
        <p class="service-text">Lorem ipsum dolor sit amet,<br>consectetuer adipiscing elit, sed diam</p>
      </li>
      <li class="service">
        <h2 class="service-title">
          <svg class="service-icon" viewBox="0 0 30 30" aria-hidden="true">
            <g fill="none" stroke="var(--brand-blue)" stroke-width="2.2">
              <rect x="3" y="3" width="24" height="7" rx="3.5"/>
              <rect x="3" y="12" width="24" height="7" rx="3.5"/>
              <rect x="3" y="21" width="24" height="7" rx="3.5"/>
            </g>
            <g fill="var(--brand-blue)">
              <circle cx="8" cy="6.5" r="1.3"/>
              <circle cx="8" cy="15.5" r="1.3"/>
              <circle cx="8" cy="24.5" r="1.3"/>
            </g>
          </svg>
          Data
        </h2>
        <p class="service-text">Lorem ipsum dolor sit amet,<br>consectetuer adipiscing elit, sed diam</p>
      </li>
    </ul>
  </section>
</div>
</body>
</html>
```